Newly opened kids play space needs brochure to show what our space has to offer

Tri-fold color brochure with same aethetic as website (www.fernhollowplayhouse.com) that provides a comprehensive and visual overview of what our play space is comprised of. Features of the brochure should include our logo, "A Steiner and Reggio-inspired Play Space in the Poconos", photos of: Dedicated Infant Play Area; Cafe and Free WiFi; Weekly Themed Activities; Unique Classes; Parties and Events. Photos also of our open play area with children playing within it. Info within the brochure should include our location, hours. Please take some copy from : https://www.facebook.com/fernhollowkinderplayhouse/?ref=bookmarks
and from the Plan Your Visit part of the website. I have a lot of photos to use; is there a way to put in generic photo placeholders and I can pick which photos of mine to go into the various areas of the brochure, or if you need the photos ahead of time, please let me know the best way to proceed. I am attaching the logo files for now.

Font styles to use
Sans Serif

Colors
85cae6
cee9f5
86cfc6
cfeae6
fdf9cf
fff3d1
eaf2ce
cadf82

Requirements
Must have
• Eye catching placement of photos; color scheme similar to website and logo colors
Should not have
• Brochure should be simple, not too colorful - no primary colors, not too crowded.

```html
<!DOCTYPE html>
<html lang="en">
<head>
<meta charset="utf-8">
<title>Fern Hollow Play Space – Brochure</title>
<link href="https://fonts.googleapis.com/css2?family=Open+Sans:wght@600;700&family=Roboto+Condensed:wght@700&family=Tinos&display=swap" rel="stylesheet">
<style>
  :root{
    --teal:#1b8fb8;
    --heading-blue:#2a92c2;
    --green:#a5c64c;
    --green-soft:#eaf2ce;
    --yellow-soft:#fdf9cf;
    --box-blue:#0b8fc0;
    --ink:#2a2a2a;
    --serif:"Tinos", "Times New Roman", serif;
    --sans:"Open Sans", Arial, sans-serif;
    --condensed:"Roboto Condensed", Arial, sans-serif;
  }
  *{box-sizing:border-box;margin:0;padding:0}
  html,body{width:1200px;height:856px;overflow:hidden;background:#fff}
  .brochure{position:relative;width:1200px;height:856px;font-family:var(--serif);color:var(--ink)}
  .panel{position:absolute;top:0;height:856px}
  .panel--back{left:0;width:398px;background:linear-gradient(to right,#fff 62%,#e6e6e6)}
  .panel--inside{left:398px;width:400px;background:linear-gradient(to right,#fff 80%,#e3e3e3)}
  .panel--cover{left:798px;width:402px;background:#fff}
  .base-bar{position:absolute;left:0;bottom:0;width:798px;height:19px;background:var(--box-blue)}

  .brand{display:flex;align-items:center;justify-content:center;gap:8px;font-family:var(--sans);font-weight:700;color:var(--teal)}
  .brand__dot{border-radius:50%;background:#86cfc6}

  .back-brand{position:absolute;left:0;width:350px;top:396px}
  .back-brand .brand{font-size:30px}
  .back-brand .brand__dot{width:22px;height:22px}
  .contact{position:absolute;left:0;width:350px;top:480px;text-align:center;font-size:12.5px;line-height:15.5px;font-style:normal}
  .contact__web{color:var(--heading-blue);letter-spacing:1.6px;font-size:10.5px;margin-top:1px}

  .feature{position:absolute;left:20px;width:341px}
  .feature--green{background:var(--green-soft)}
  .feature--yellow{background:var(--yellow-soft)}
  .photo{position:absolute}
  .feature__title{position:absolute;color:var(--heading-blue);font-size:20px;line-height:23px;font-weight:400}
  .feature__title--sans{font-family:var(--sans);font-weight:700;font-size:18px}
  .feature__text{position:absolute;font-size:14px;line-height:16.3px}

  .cover-brand{position:absolute;left:0;width:402px;top:128px}
  .cover-brand .brand{font-size:42px}
  .cover-brand .brand__dot{width:28px;height:28px}
  .tagline{position:absolute;top:220px;width:402px;text-align:center;font-family:var(--sans);font-weight:700;color:var(--green);font-size:29px}
  .intro-band{position:absolute;top:272px;left:0;width:402px;height:46px;background:var(--green);color:#fff;font-family:var(--condensed);font-weight:700;font-size:15px;line-height:18px;text-align:center;padding-top:5px}
  .hero{top:318px;left:0;width:402px;height:205px}

  .offer{position:absolute;top:553px;left:33px;width:340px;height:118px}
  .offer__band{position:absolute;left:133px;top:0;width:207px;height:118px;background:var(--green)}
  .thumb{position:absolute;width:64px;height:56px;border:2px solid #cadf82}
  .offer__list{position:absolute;left:180px;top:2px;list-style:none;color:#fff;font-family:var(--sans);font-weight:700;font-size:13px;line-height:23.5px}
  .offer__list li::before{content:"•";margin-left:-18px;margin-right:12px}

  .hours{position:absolute;top:701px;left:30px;width:349px;height:99px;background:var(--box-blue);border-radius:4px;color:#fff;display:flex}
  .hours__col{padding:5px 0 0 22px}
  .hours__col+.hours__col{border-left:1px solid #9fd3e6;margin:12px 0;padding-top:0;padding-left:28px}
  .hours__title{font-size:17px;line-height:22px}
  .hours__line{font-size:11.5px;line-height:16px}
  .cover-web{position:absolute;top:824px;left:34px;width:340px;display:flex;justify-content:space-between;font-size:11px;color:var(--heading-blue)}
</style>
</head>
<body>
<div class="brochure">
  <section class="panel panel--back">
    <div class="back-brand"><div class="brand"><span class="brand__dot"></span>Fern Hollow</div></div>
    <address class="contact">
      <div>(570) 555-0148</div>
      <div>42 Laurel Bend Road,</div>
      <div>Cresco Falls, PA 18399</div>
      <div class="contact__web">www.fernhollowplayhouse.com</div>
    </address>
  </section>

  <section class="panel panel--inside">
    <div class="feature feature--green" style="top:39px;height:155px">
      <div class="photo" role="img" aria-label="Photo: parent enjoying coffee in the café lounge" style="left:1px;top:9px;width:161px;height:138px;background:linear-gradient(135deg,#6b5a4a,#b48d6a 60%,#8a6e55)"></div>
      <h2 class="feature__title feature__title--sans" style="left:181px;top:16px">Café and WIFI</h2>
      <p class="feature__text" style="left:181px;top:40px;width:145px">Take a break or catch up on work while enjoying Ridgeline coffee, beverages, and healthy snacks.</p>
    </div>
    <div class="feature feature--yellow" style="top:194px;height:166px">
      <h2 class="feature__title" style="left:8px;top:17px">Dedicated<br>Infant Area</h2>
      <p class="feature__text" style="left:5px;top:70px;width:180px">Bond safely with your baby while being within eyeshot of the main play area.</p>
      <div class="photo" role="img" aria-label="Photo: parent and baby in the infant area" style="left:191px;top:35px;width:145px;height:124px;background:linear-gradient(135deg,#c9b49a,#7a6a5c 55%,#2f3440)"></div>
    </div>
    <div class="feature feature--green" style="top:360px;height:154px">
      <div class="photo" role="img" aria-label="Photo: children planting flowers during a themed activity" style="left:1px;top:12px;width:161px;height:124px;background:linear-gradient(135deg,#8a8680,#c8c3bb 50%,#6e7b4e)"></div>
      <h2 class="feature__title" style="left:175px;top:11px">Themed Activities</h2>
      <p class="feature__text" style="left:177px;top:40px;width:162px">Stories, crafts, and activities change weekly to celebrate the seasons and the world around us.</p>
    </div>
    <div class="feature feature--yellow" style="top:514px;height:162px">
      <h2 class="feature__title" style="left:10px;top:12px">Unique Classes</h2>
      <p class="feature__text" style="left:10px;top:46px;width:160px">Our multi-age, multi-sensory approach to traditional classes nurtures the whole child in a creative and fun way.</p>
      <div class="photo" role="img" aria-label="Photo: group class seated in a circle on a rug" style="left:187px;top:25px;width:148px;height:113px;background:linear-gradient(135deg,#c2744a,#8a5c8c 50%,#c8a04a)"></div>
    </div>
    <div class="feature feature--green" style="top:676px;height:156px">
      <div class="photo" role="img" aria-label="Photo: party favours for an event" style="left:5px;top:10px;width:155px;height:118px;background:linear-gradient(135deg,#1e2040,#c9b43a 50%,#b23a6a)"></div>
      <h2 class="feature__title" style="left:194px;top:12px">Parties and<br>Events</h2>
      <p class="feature__text" style="left:194px;top:63px;width:145px">Take a break or catch up on work while enjoying Ridgeline coffee, beverages, and healthy snacks.</p>
    </div>
  </section>

  <section class="panel panel--cover">
    <div class="cover-brand"><div class="brand"><span class="brand__dot"></span>Fern Hollow</div></div>
    <p class="tagline">Play. Learn. Grow.</p>
    <div class="intro-band">We are a Woodland and Reggio-inspired<br>play space located in the Poconos.</div>
    <div class="photo hero" role="img" aria-label="Photo: children playing in the open play area" style="background:linear-gradient(135deg,#b98f6a,#8e6a4c 45%,#1f2a5a 85%)"></div>

    <div class="offer">
      <div class="offer__band"></div>
      <div class="thumb" role="img" aria-label="Thumbnail: café" style="left:0;top:0;background:linear-gradient(135deg,#6b5a4a,#b48d6a)"></div>
      <div class="thumb" role="img" aria-label="Thumbnail: infant area" style="left:70px;top:0;background:linear-gradient(135deg,#c9b49a,#2f3440)"></div>
      <div class="thumb" role="img" aria-label="Thumbnail: themed activities" style="left:0;top:60px;background:linear-gradient(135deg,#8a8680,#6e7b4e)"></div>
      <div class="thumb" role="img" aria-label="Thumbnail: classes" style="left:70px;top:60px;background:linear-gradient(135deg,#c2744a,#8a5c8c)"></div>
      <ul class="offer__list">
        <li>Café and WIFI</li>
        <li>Dedicated Infant Area</li>
        <li>Themed Activities</li>
        <li>Unique Classes</li>
        <li>Parties and Events</li>
      </ul>
    </div>

    <div class="hours">
      <div class="hours__col" style="width:164px">
        <div class="hours__title">Open Play</div>
        <div class="hours__line">Mon, Wed, Fri, Sun</div>
        <div class="hours__line">10:00AM - 5:00PM</div>
        <div class="hours__line">Tue, Thu, Sat</div>
        <div class="hours__line">10:00AM - 7:00PM</div>
      </div>
      <div class="hours__col">
        <div class="hours__title">Infants Only</div>
        <div class="hours__line">Monday through Friday</div>
        <div class="hours__line">9:00AM - 10:00AM</div>
      </div>
    </div>
    <div class="cover-web"><span>w</span><span>w</span><span>w</span><span>.</span><span>f</span><span>e</span><span>r</span><span>n</span><span>h</span><span>o</span><span>l</span><span>l</span><span>o</span><span>w</span><span>p</span><span>l</span><span>a</span><span>y</span><span>h</span><span>o</span><span>u</span><span>s</span><span>e</span><span>.</span><span>c</span><span>o</span><span>m</span></div>
  </section>

  <div class="base-bar"></div>
</div>
</body>
</html>
```